Looking for a high-end business card design for a construction company

We are looking to update our business card design. We are a post-frame construction company that builds custom buildings, commercial spaces, homes, and anything else. We have multiple people working here so we would need something we can easily customize the information for the specific person. We need a name, website, cell phone, office phone as well as social icons. Our colors are black, white, and grey/silver so I would love a black background or something that is more striking than just a traditional white business card. Looking for something that is very professional with a high-end look/feel. I have attached our logos, they can be silver, white, grey, or black.
Industry/Entity Type
Construction
Contact Information for Business Card
Business logo, Name, Cell phone, Office phone, website, social Icons
Colors
Designer to choose only greyscale colors for use in the design.
Look and feel

```html
<!DOCTYPE html>
<html lang="en">
<head>
<meta charset="utf-8">
<title>Harrow Post Frame, Inc. — Business Card</title>
<link rel="stylesheet" href="https://fonts.googleapis.com/css2?family=Arimo:wght@400;700&display=swap">
<style>
  :root {
    --canvas: #6e6f6f;
    --ink: #0c0c0c;
    --paper: #ffffff;
    --paper-shade: #ededed;
    --text: #1a1a1a;
    --muted: #3a3a3a;
    --silver: #cfcfcf;
  }
  * { box-sizing: border-box; margin: 0; padding: 0; }
  html, body { width: 1200px; height: 907px; overflow: hidden; }
  body {
    background: radial-gradient(ellipse at 50% 45%, #7c7d7d 0%, var(--canvas) 70%);
    font-family: "Arimo", Arial, sans-serif;
    position: relative;
  }
  .card {
    position: absolute;
    top: 300px;
    width: 530px;
    height: 306px;
    border-radius: 22px;
    overflow: hidden;
    box-shadow: 0 14px 30px rgba(0,0,0,0.35);
  }
  /* Front */
  .card-front {
    left: 50px;
    background: linear-gradient(160deg, #1c1c1c 0%, var(--ink) 55%, #050505 100%);
    color: var(--paper);
  }
  .front-brand {
    position: absolute;
    left: 0; right: 0; top: 104px;
    display: flex; align-items: center; justify-content: center; gap: 14px;
  }
  .brand-dot {
    width: 30px; height: 30px; border-radius: 50%;
    background: var(--paper);
    flex: none;
  }
  .brand-name {
    font-weight: 700;
    font-size: 30px;
    letter-spacing: 3px;
    text-transform: uppercase;
    line-height: 1.05;
  }
  .brand-name small { display: block; font-size: 19px; letter-spacing: 4px; }
  .front-web {
    position: absolute;
    left: 0; right: 0; bottom: 38px;
    text-align: center;
    font-size: 14px;
    color: var(--silver);
  }
  /* Back */
  .card-back {
    left: 620px;
    background: linear-gradient(180deg, var(--paper) 0%, var(--paper-shade) 100%);
    color: var(--text);
  }
  .back-swoosh { position: absolute; inset: 0; }
  .back-brand {
    position: absolute;
    left: 40px; top: 64px;
    display: flex; align-items: center; gap: 14px;
    color: var(--ink);
  }
  .back-brand .brand-dot { background: var(--ink); width: 40px; height: 40px; }
  .back-brand .brand-name { font-size: 26px; }
  .back-brand .brand-name small { font-size: 16px; }
  .person {
    position: absolute;
    left: 96px; top: 178px;
  }
  .person-name { font-size: 21px; font-weight: 400; }
  .person-title { font-size: 14px; color: var(--muted); margin-top: 3px; padding-left: 22px; }
  .contact {
    position: absolute;
    left: 280px; top: 118px;
    font-size: 13.5px;
    line-height: 1.3;
    list-style: none;
  }
  .contact .address { margin-bottom: 6px; padding-left: 24px; }
  .contact li { display: flex; align-items: center; gap: 8px; }
  .contact svg { width: 13px; height: 13px; flex: none; fill: var(--ink); }
</style>
</head>
<body>

<section class="card card-front" aria-label="Card front">
  <div class="front-brand">
    <span class="brand-dot"></span>
    <div class="brand-name">Harrow<small>Post Frame, Inc.</small></div>
  </div>
  <p class="front-web">www.harrowpf.com</p>
</section>

<section class="card card-back" aria-label="Card back">
  <svg class="back-swoosh" viewBox="0 0 530 306" preserveAspectRatio="none" aria-hidden="true">
    <path d="M360 0 Q470 20 530 120 L530 0 Z" fill="#0c0c0c"/>
    <path d="M380 0 Q480 30 530 135 L530 120 Q470 20 360 0 Z" fill="#9a9a9a"/>
    <path d="M0 170 Q60 285 200 306 L0 306 Z" fill="#0c0c0c"/>
    <path d="M0 150 Q55 280 215 306 L200 306 Q60 285 0 170 Z" fill="#9a9a9a"/>
  </svg>

  <div class="back-brand">
    <span class="brand-dot"></span>
    <div class="brand-name">Harrow<small>Post Frame, Inc.</small></div>
  </div>

  <div class="person">
    <p class="person-name">Daniel Reyes</p>
    <p class="person-title">President</p>
  </div>

  <ul class="contact">
    <li class="address">48 Millbrook Lane<br>Cedar Falls, IA 50613</li>
    <li><svg viewBox="0 0 16 16"><path d="M3 2h3l1 4-2 1a9 9 0 0 0 4 4l1-2 4 1v3a1 1 0 0 1-1 1A13 13 0 0 1 2 3a1 1 0 0 1 1-1z"/></svg>020 7946 0321</li>
    <li><svg viewBox="0 0 16 16"><path d="M5 1h6a1 1 0 0 1 1 1v12a1 1 0 0 1-1 1H5a1 1 0 0 1-1-1V2a1 1 0 0 1 1-1zm0 2v9h6V3z"/></svg>020 7946 0322</li>
    <li><svg viewBox="0 0 16 16"><path d="M2 4h12v8H2z M4 6v4h8V6z"/></svg>020 7946 0323</li>
    <li><svg viewBox="0 0 16 16"><path d="M1 3h14v10H1zm1.5 1.5L8 9l5.5-4.5z"/></svg>d.reyes@harrowpf.com</li>
    <li><svg viewBox="0 0 16 16"><circle cx="8" cy="8" r="7"/></svg>www.harrowpf.com</li>
  </ul>
</section>

</body>
</html>
```